"Hollow Lanterns" Women's Fiction Book Cover

The title of the book is "Hollow Lanterns," and the author name is M.L. Dorn. It's women's fiction, but with a subtle supernatural flair. I'm just looking for something that fits the back cover copy (below). Surprise me!

When fleeing your past leads you straight to your future...
Lucinda Marwell's seemingly perfect life in Ashmont Heights comes crashing down around her when her fiancé announces that he’s in love with her cousin. Heartbroken and reckless, she crashes her car on a winding coastal road—an accident that should have killed, or at least paralyzed her. Instead, she awakens mysteriously unharmed, rescued by what she initially believes to be an angel. Later, she finds out her hero is an enigmatic Irish paramedic named Tobias.
Stranded in the idyllic town of Fernwick Cove, Lucinda finds herself working at a charming inn and, for the first time, feeling like she belongs somewhere. The close-knit community embraces her, and she’s drawn to Tobias despite his obvious secrets. But Tobias is running from a dangerous past—his supernatural gift of healing nearly cost him everything when he couldn’t save a Chicago mob boss’s son.
As Lucinda and Tobias grow closer, Tobias struggles to keep his abilities hidden. But when stories of miraculous healings in Fernwick Cove begin surfacing on social media, his past catches up with him. When a Chicago reporter sent by a vengeful mob boss closes in, Tobias must choose between protecting his secret and finally facing up to his fears.
In a town where everyone knows everyone else's business, some secrets are too powerful to stay buried.
A heartwarming tale of second chances, supernatural gifts, and finding home in the most unexpected places.

Target Market(s)

women ages 20-70

Requirements
Must have
• illustrated, brightly colored, whimsical
Nice to have
• see description

```html
<!DOCTYPE html>
<html lang="en">
<head>
<meta charset="UTF-8">
<title>Hollow Lanterns — Full Wrap Cover</title>
<link rel="stylesheet" href="https://fonts.googleapis.com/css2?family=Amatic+SC:wght@700&family=Montserrat:wght@400&display=swap">
<style>
  :root {
    --paper: #ffffff;
    --cover-blue: #034ea2;
    --title-sand: #e8c98e;
    --author-mint: #4fd08e;
    --rule-teal: #2a8fa0;
    --photo-slot: #1e6fa0;
    --body-white: #ffffff;
  }
  * { margin: 0; padding: 0; box-sizing: border-box; }
  html, body {
    width: 1200px; height: 844px; overflow: hidden;
    background: var(--paper);
  }
  .wrap-cover {
    position: absolute; left: 22px; top: 22px;
    width: 1156px; height: 800px;
    background: var(--cover-blue);
    overflow: hidden;
  }
  .title-font { font-family: "Amatic SC", "Arial Narrow", sans-serif; font-weight: 700; color: var(--title-sand); }
  .text-font { font-family: "Montserrat", Arial, sans-serif; font-weight: 400; }

  /* Back cover */
  .back-title {
    position: absolute; left: 43px; width: 454px; top: 44px;
    text-align: center; font-size: 38px; letter-spacing: 1px; line-height: 1;
  }
  .copy-block {
    position: absolute;
    color: var(--body-white); font-size: 12.4px; line-height: 18.8px;
  }
  .copy-block .line {
    display: block; height: 18.8px; white-space: nowrap; overflow: hidden;
    text-align: justify; text-align-last: justify;
  }
  .copy-block .line.end { text-align-last: left; }
  .blurb { left: 43px; top: 100px; width: 454px; }
  .rule {
    position: absolute; left: 42px; width: 456px; height: 1px;
    background: var(--rule-teal);
  }
  .rule-top { top: 446px; }
  .rule-bottom { top: 636px; }
  .author-photo {
    position: absolute; left: 50px; top: 465px; width: 126px; height: 154px;
    background: var(--photo-slot);
  }
  .author-bio { left: 194px; top: 464px; width: 303px; }

  /* Spine */
  .spine-title, .spine-author {
    position: absolute; writing-mode: vertical-rl; white-space: nowrap; line-height: 1;
  }
  .spine-title { left: 556px; top: 50px; font-size: 54px; letter-spacing: 1px; }
  .spine-author {
    left: 565px; top: 541px; font-size: 29px; color: var(--author-mint); letter-spacing: 1px;
  }

  /* Front cover */
  .front-title {
    position: absolute; left: 690px; top: 40px; width: 400px;
    text-align: center; font-size: 146px; line-height: 132px; letter-spacing: 2px;
  }
  .front-art {
    position: absolute; left: 512px; top: 318px; width: 640px; height: 380px;
    background:
      radial-gradient(ellipse 40% 30% at 55% 45%, #e9f7c8 0%, rgba(233,247,200,0) 100%),
      linear-gradient(180deg, #5f6a9e 0%, #6c83c8 25%, #7fb6e0 45%, #5fd890 62%, #3fbfa0 80%, rgba(3,78,162,0) 100%);
    -webkit-mask-image: radial-gradient(ellipse 52% 55% at 58% 55%, #000 60%, transparent 100%);
            mask-image: radial-gradient(ellipse 52% 55% at 58% 55%, #000 60%, transparent 100%);
  }
  .front-author {
    position: absolute; left: 760px; top: 704px; width: 280px;
    text-align: center; font-size: 39px; color: var(--author-mint);
    letter-spacing: 2px; line-height: 1;
  }
</style>
</head>
<body>
  <main class="wrap-cover">
    <section class="back-cover">
      <h2 class="back-title title-font">HOLLOW LANTERNS</h2>
      <div class="copy-block blurb text-font">
        <span class="line">Lorem ipsum dolor sit amet, consectetuer adipiscing elit, sed diam</span>
        <span class="line">nonummy nibh euismod tincidunt ut laoreet dolore magna aliquam</span>
        <span class="line">erat volutpat. Ut wisi enim ad minim veniam, quis nostrud exerci tation</span>
        <span class="line">ullamcorper suscipit lobortis nisl ut aliquip ex ea commodo consequat.</span>
        <span class="line">Duis autem vel eum iriure dolor in hendrerit in vulputate velit esse</span>
        <span class="line">molestie consequat, vel illum dolore eu feugiat nulla facilisis at vero</span>
        <span class="line">eros et accumsan et iusto odio dignissim qui blandit praesent luptatum</span>
        <span class="line end">.zzril delenit augue duis dolore te feugait nulla facilisi</span>
        <span class="line">Lorem ipsum dolor sit amet, cons ectetuer adipiscing elit, sed diam</span>
        <span class="line">nonummy nibh euismod tincidunt ut laoreet dolore magna aliquam</span>
        <span class="line">erat volutpat. Ut wisi enim ad minim veniam, quis nostrud exerci tation</span>
        <span class="line">.ullamcorper suscipit lobortis nisl ut aliquip ex ea commodo consequat</span>
        <span class="line">Lorem ipsum dolor sit amet, consectetuer adipiscing elit, sed diam</span>
        <span class="line">nonummy nibh euismod tincidunt ut laoreet dolore magna aliquam</span>
        <span class="line">erat volutpat. Ut wisi enim ad minim veniam, quis nostrud exerci tation</span>
        <span class="line">ullamcorper suscipit lobortis nisl ut aliquip ex ea commodo consequat.</span>
        <span class="line">Duis autem vel eum iriure dolor in hendrerit in vulputate velit esse</span>
      </div>
      <div class="rule rule-top"></div>
      <div class="author-photo" role="img" aria-label="Author portrait placeholder"></div>
      <div class="copy-block author-bio text-font">
        <span class="line">Lorem ipsum dolor sit amet, consectetuer</span>
        <span class="line">adipiscing elit, sed diam nonummy nibh euis-</span>
        <span class="line">mod tincidunt ut laoreet dolore magna aliquam</span>
        <span class="line">erat volutpat. Ut wisi enim ad minim veniam,</span>
        <span class="line">quis nostrud exerci tation ullamcorper suscipit</span>
        <span class="line">lobortis nisl ut aliquip ex ea commodo conse-</span>
        <span class="line">quat. Duis autem vel eum iriure dolor in hen-</span>
        <span class="line">drerit in vulputate velit esse molestie conse-</span>
      </div>
      <div class="rule rule-bottom"></div>
    </section>

    <section class="spine">
      <span class="spine-title title-font">HOLLOW LANTERNS</span>
      <span class="spine-author text-font">M.L. DORN</span>
    </section>

    <section class="front-cover">
      <h1 class="front-title title-font">HOLLOW<br>LANTERNS</h1>
      <div class="front-art" role="img" aria-label="Illustration of a man walking a golden dog and a blonde girl on a green coastal hillside path above a bay at dusk, with a tree and distant hills"></div>
      <p class="front-author text-font">M.L. DORN</p>
    </section>
  </main>
</body>
</html>
```